Upscale business cards needed for family office

We would like professional business cards created for employees of our family office. Relatively simple and straightforward, but also with a unique element to set them apart. Probably stick with neutral and simple colors that mesh well with the colors in the logo. We need space for the traditional elements, including name, title, address, email/phone number.

Industry/Entity Type

Business

Contact Information for Business Card

Space for name, title, phone number, email, address

```html
<!DOCTYPE html>
<html lang="en">
<head>
<meta charset="utf-8">
<title>Marlow &amp; Reed business card</title>
<link rel="stylesheet" href="https://fonts.googleapis.com/css2?family=Roboto:wght@400&family=Tinos:wght@400;700&display=swap">
<style>
  :root {
    --backdrop: #e4e5e8;
    --card: #ffffff;
    --ink: #3f4850;
    --ink-soft: #5a6068;
    --teal: #1b9cc8;
    --sea: #0f9bc9;
    --navy: #3e6fb6;
  }
  * { box-sizing: border-box; margin: 0; padding: 0; }
  html, body { width: 1200px; height: 800px; overflow: hidden; }
  body {
    background: var(--backdrop);
    font-family: "Roboto", Arial, sans-serif;
    position: relative;
  }
  .card {
    position: absolute;
    top: 252px;
    width: 520px;
    height: 297px;
    background: var(--card);
    box-shadow: 0 6px 18px rgba(0,0,0,.12);
    overflow: hidden;
  }
  .card--front { left: 50px; }
  .card--back { left: 630px; }

  .card__waves { position: absolute; inset: 0; width: 100%; height: 100%; }

  .holder { position: absolute; left: 44px; top: 22px; }
  .holder__name {
    font-family: "Tinos", "Times New Roman", serif;
    font-weight: 700;
    font-size: 22px;
    color: var(--ink);
    line-height: 1;
  }
  .holder__title {
    font-size: 12px;
    color: var(--teal);
    margin-top: 3px;
  }
  .contact { list-style: none; margin-top: 6px; }
  .contact__item {
    display: flex;
    align-items: center;
    gap: 6px;
    font-size: 11.5px;
    color: var(--ink-soft);
    line-height: 16px;
  }
  .contact__icon { width: 9px; height: 9px; flex: none; }

  .address {
    position: absolute;
    left: 44px;
    top: 206px;
    font-family: "Tinos", "Times New Roman", serif;
    font-style: normal;
    font-size: 12px;
    line-height: 14px;
    color: #ffffff;
  }

  .brand {
    position: absolute;
    display: flex;
    align-items: center;
    gap: 8px;
    font-family: "Tinos", "Times New Roman", serif;
    font-weight: 400;
    color: var(--ink);
    white-space: nowrap;
  }
  .brand__mark { flex: none; background: var(--navy); }
  .card--front .brand { left: 322px; top: 166px; font-size: 20px; }
  .card--front .brand__mark { width: 14px; height: 14px; }
  .card--back .brand {
    left: 50%; top: 50%;
    transform: translate(-50%, -50%);
    font-size: 26px;
  }
  .card--back .brand__mark { width: 18px; height: 18px; }
</style>
</head>
<body>

<article class="card card--front">
  <svg class="card__waves" viewBox="0 0 520 297" preserveAspectRatio="none" aria-hidden="true">
    <path fill="var(--navy)" d="M0,150 C160,148 250,205 310,245 C360,275 450,280 520,282 L520,297 L0,297 Z"/>
    <path fill="var(--sea)" stroke="#ffffff" stroke-width="4" d="M-4,172 C140,170 230,215 290,252 C340,282 440,288 524,290 L524,301 L-4,301 Z"/>
  </svg>

  <div class="holder">
    <h1 class="holder__name">Daniel Hart</h1>
    <p class="holder__title">Managing director</p>
    <ul class="contact">
      <li class="contact__item">
        <svg class="contact__icon" viewBox="0 0 10 10"><path fill="var(--ink)" d="M2,0 L4,2.5 L3,3.6 Q4.3,6 6.4,7 L7.5,6 L10,8 L8.6,9.8 Q2,9 0.2,1.4 Z"/></svg>
        0781-2290-4413
      </li>
      <li class="contact__item">
        <svg class="contact__icon" viewBox="0 0 10 10"><rect x="2.5" y="0.5" width="5" height="3" fill="none" stroke="var(--ink)"/><rect x="0" y="3.5" width="10" height="4.5" rx="1" fill="var(--ink)"/><rect x="2.5" y="6.5" width="5" height="3" fill="#fff" stroke="var(--ink)"/></svg>
        0745-6612-3098
      </li>
      <li class="contact__item">
        <svg class="contact__icon" viewBox="0 0 10 10"><rect x="0.5" y="1.5" width="9" height="7" fill="none" stroke="var(--ink)"/><path d="M0.5,1.5 L5,5.5 L9.5,1.5" fill="none" stroke="var(--ink)"/></svg>
        dhart@marlowreed.com
      </li>
      <li class="contact__item">
        <svg class="contact__icon" viewBox="0 0 10 10"><rect x="0.5" y="0.5" width="9" height="6.5" fill="none" stroke="var(--ink)"/><path d="M3,9.5 H7" stroke="var(--ink)"/></svg>
        marlowreed.com
      </li>
    </ul>
  </div>

  <address class="address">
    240 Harbor Lane, Suite 100<br>
    City, State, Zip Code
  </address>

  <div class="brand"><span class="brand__mark"></span>Marlow &amp; Reed</div>
</article>

<article class="card card--back">
  <div class="brand"><span class="brand__mark"></span>Marlow &amp; Reed</div>
</article>

</body>
</html>
```